Management consulting Company in the electronic payment ecosystem needs a Website

We need to have a "showcase" style website that contains the key message that our company is able to provide management consulting in the world of payment systems. Our mission is to assist our clients in reviewing their sales, purchasing, operation and IT processes and to support them in identifying the best solution in the use of payment systems.

```html
<!DOCTYPE html>
<html lang="en">
<head>
<meta charset="utf-8">
<title>Veridan Consulting – Payment Systems Consulting</title>
<link href="https://fonts.googleapis.com/css2?family=Poppins:wght@300;400;500;600;700&display=swap" rel="stylesheet">
<style>
:root{
  --navy:#0d1b5e;
  --navy-deep:#0a1550;
  --bar:#1a3aa8;
  --white:#ffffff;
  --ink:#0d1b5e;
  --text:#2a3470;
  --muted:#c9d0ee;
  --photo-a:#3a4f8c;
  --photo-b:#c89a6a;
}
*{margin:0;padding:0;box-sizing:border-box}
html,body{width:1200px;height:4549px;overflow:hidden}
body{font-family:'Poppins',sans-serif;color:var(--ink);background:var(--white);position:relative}
.sec{position:absolute;left:0;width:1200px;overflow:hidden}
.abs{position:absolute}
.navy{background:var(--navy);color:var(--white)}
.btn{position:absolute;display:flex;align-items:center;justify-content:center;border-radius:20px;font-size:11px;font-weight:400}
.btn-ghost{border:1.5px solid var(--white);color:var(--white)}
.btn-solid{background:var(--white);color:var(--ink)}
.btn-dark{background:var(--navy);color:var(--white)}
.btn-outline{border:1.5px solid var(--ink);color:var(--ink)}
.photo{position:absolute;border-radius:50%}
.ring{position:absolute;border-radius:50%;border:2px solid var(--navy)}
.ring-w{border-color:var(--white)}
/* header */
.brand{position:absolute;display:flex;align-items:center;gap:8px;color:var(--white);font-weight:600}
.brand-dot{width:44px;height:44px;border-radius:50%;background:var(--white)}
.brand-name{font-size:30px;line-height:1}
.nav{position:absolute;top:44px;font-size:11px;font-weight:600;letter-spacing:.3px}
.hero-title{left:141px;top:213px;width:380px;font-size:26px;line-height:31px;font-weight:500}
.hero-dots{left:141px;top:318px;letter-spacing:3px;font-size:14px;line-height:8px}
.hero-text{left:141px;top:338px;width:370px;font-size:11px;line-height:16.2px}
/* insight */
.insight-title{left:621px;top:764px;font-size:27px;font-weight:700}
.insight-text{left:621px;top:810px;width:445px;font-size:12px;line-height:20.5px;color:var(--text)}
/* articles */
.card{position:absolute;top:1093px;width:270px}
.card h3{font-size:16px;line-height:24px;font-weight:500;height:84px;margin-top:298px}
.card p{font-size:12px;line-height:20.4px;margin-top:4px}
/* stats */
.stat{position:absolute;top:1800px;width:240px;text-align:center}
.stat b{display:block;font-size:48px;font-weight:300;line-height:60px}
.stat span{font-size:12px}
.divider{position:absolute;top:1814px;width:2px;height:58px;background:var(--ink)}
.stats-text{left:300px;top:1908px;width:600px;text-align:center;font-size:12px;line-height:20px;color:var(--text)}
/* features */
.feat{position:absolute;width:260px;text-align:center}
.feat svg{display:block;margin:0 auto 6px}
.feat h4{font-size:14px;font-weight:500}
.feat p{font-size:11px;line-height:17px;margin-top:4px}
/* testimonial */
.quote{font-size:110px;line-height:1;color:#d6d9e6;font-family:Georgia,serif}
.testi-title{left:0;width:1200px;top:3026px;text-align:center;font-size:26px;font-weight:700}
.testi-text{left:255px;top:3080px;width:690px;text-align:center;font-size:11.5px;line-height:17px;color:var(--text)}
.testi-name{left:0;width:1200px;top:3161px;text-align:center;font-size:12px;font-weight:600}
.testi-role{left:0;width:1200px;top:3180px;text-align:center;font-size:9px;color:var(--text)}
/* contact */
.field{position:absolute;left:141px;width:487px;border:1.5px solid var(--white);border-radius:20px;font-size:12px;padding:8px 18px;color:var(--white)}
/* footer */
.foot-col{position:absolute;top:4350px;font-size:10px;line-height:18px;color:var(--white)}
.foot-col h5{font-size:12px;font-weight:600;margin-bottom:2px}
.sub-field{position:absolute;left:865px;width:190px;height:32px;border:1.5px solid var(--white);border-radius:16px;font-size:11px;color:var(--white);text-align:right;padding:6px 24px}
.social{position:absolute;top:4476px;width:24px;height:24px;border:1.5px solid var(--white);border-radius:50%}
</style>
</head>
<body>

<!-- Hero -->
<section class="sec navy" style="top:0;height:674px">
  <div class="ring ring-w" style="left:524px;top:74px;width:700px;height:700px"></div>
  <div class="photo" role="img" aria-label="Smiling couple paying online with a card and phone" style="left:605px;top:120px;width:678px;height:678px;background:radial-gradient(circle at 45% 45%,var(--photo-b),#6b5240 45%,var(--photo-a))"></div>
  <div class="brand" style="left:141px;top:22px"><span class="brand-dot"></span><span class="brand-name">Veridan</span></div>
  <div class="nav" style="left:748px">SERVICES</div>
  <div class="nav" style="left:833px">ABOUT US</div>
  <div class="nav" style="left:923px">FAQ</div>
  <div class="nav" style="left:972px">CONTACT US</div>
  <h1 class="abs hero-title">Lorem ipsum dolor sit amet consectetur adipiscing elit sed do eiusmod</h1>
  <div class="abs hero-dots">•••</div>
  <p class="abs hero-text">Lorem ipsum dolor sit amet, consectetur adipiscing elit, sed do eiusmod tempor incididunt ut labore et dolore magna aliqua. Ut enim ad minim veniam, quis nostrud exercitation ullamco laboris nisi ut aliquip ex ea commodo consequat. Duis aute irure dolor in reprehenderit in voluptate velit esse cillum dolore eu fugiat nulla pariatur. Excepteur sint occaecat cupidatat non proident, sunt in culpa qui officia deserunt mollit anim id est laborum.</p>
  <div class="btn btn-ghost" style="left:141px;top:476px;width:118px;height:32px">Learn More</div>
  <div class="btn btn-solid" style="left:277px;top:476px;width:118px;height:32px">Contact Us</div>
  <svg class="abs" style="left:420px;top:484px" width="18" height="14" viewBox="0 0 18 14"><path d="M3 4l6 6 6-6" stroke="#fff" stroke-width="2.5" fill="none"/></svg>
</section>

<!-- Insights -->
<section class="sec" style="top:674px;height:427px">
  <div class="ring" style="left:157px;top:34px;width:356px;height:356px"></div>
  <div class="photo" role="img" aria-label="Hands holding a phone making an online card payment at a laptop" style="left:165px;top:42px;width:340px;height:340px;background:linear-gradient(135deg,#b9c3d8,#5c6f9c 60%,#2a3a70)"></div>
</section>
<h2 class="abs insight-title">Insights on Financial Services</h2>
<p class="abs insight-text">Lorem ipsum dolor sit amet, consectetur adipiscing elit, sed do eiusmod tempor incididunt ut labore et dolore magna aliqua. Ut enim ad minim veniam, quis nostrud exercitation ullamco laboris nisi ut aliquip ex ea commodo consequat. Duis aute irure dolor in reprehenderit in voluptate velit esse cillum dolore eu fugiat nulla pariatur. Excepteur sint occaecat cupidatat non proident, sunt in culpa qui officia deserunt mollit anim id est laborum.</p>
<div class="btn btn-outline" style="left:621px;top:972px;width:119px;height:34px">Learn More</div>

<!-- Articles -->
<section class="sec navy" style="top:1101px;height:655px">
  <div class="ring ring-w" style="left:170px;top:79px;width:190px;height:190px"></div>
  <div class="photo" role="img" aria-label="Hand holding a phone showing a successful payment" style="left:177px;top:86px;width:176px;height:176px;background:radial-gradient(circle,#7fb4e8,#2a4f9a 60%,#0f2260)"></div>
  <div class="ring ring-w" style="left:502px;top:79px;width:190px;height:190px"></div>
  <div class="photo" role="img" aria-label="Glowing shopping cart above a tablet" style="left:509px;top:86px;width:176px;height:176px;background:radial-gradient(circle,#e8b24a,#5a3a1e 55%,#1a1410)"></div>
  <div class="ring ring-w" style="left:832px;top:79px;width:190px;height:190px"></div>
  <div class="photo" role="img" aria-label="Person typing on a laptop" style="left:839px;top:86px;width:176px;height:176px;background:radial-gradient(circle,#e9e6e0,#a7a39a 60%,#5a5750)"></div>
</section>
<div class="card" style="left:141px;color:#fff"><h3>Global Insurance Pools statistics and trends: An overview of life, P&amp;C, and health insurance</h3><p>Lorem ipsum dolor sit amet, consectetur adipiscing elit, sed do eiusmod tempor incididunt ut labore et dolore magna aliqua. Ut enim ad minim veniam, quis nostrud exercitation ullamco laboris nisi ut aliquip ex ea commodo consequat.</p></div>
<div class="card" style="left:470px;color:#fff"><h3>How insurers can act on the opportunity of digital eco systems</h3><p>Lorem ipsum dolor sit amet, consectetur adipiscing elit, sed do eiusmod tempor incididunt ut labore et dolore magna aliqua. Ut enim ad minim veniam, quis nostrud exercitation ullamco laboris nisi ut aliquip ex ea commodo consequat.</p></div>
<div class="card" style="left:798px;color:#fff"><h3>Revolutionizing insurance: The personalized insurance engine</h3><p>Lorem ipsum dolor sit amet, consectetur adipiscing elit, sed do eiusmod tempor incididunt ut labore et dolore magna aliqua. Ut enim ad minim veniam, quis nostrud exercitation ullamco laboris nisi ut aliquip ex ea commodo consequat.</p></div>
<div class="btn btn-ghost" style="left:141px;top:1615px;width:97px;height:28px">Read More</div>
<div class="btn btn-ghost" style="left:470px;top:1615px;width:97px;height:28px">Read More</div>
<div class="btn btn-ghost" style="left:798px;top:1615px;width:97px;height:28px">Read More</div>

<!-- Stats -->
<section class="sec" style="top:1756px;height:600px">
  <div class="ring" style="left:144px;top:302px;width:912px;height:912px"></div>
  <div class="photo" role="img" aria-label="Finger tapping payment options on a touch terminal" style="left:170px;top:318px;width:860px;height:860px;background:linear-gradient(160deg,#d9dde6,#7b8294 45%,#3b4150)"></div>
</section>
<div class="stat" style="left:185px"><b>135</b><span>Companies helped</span></div>
<div class="divider" style="left:446px"></div>
<div class="stat" style="left:448px"><b>60%</b><span>Y.O.Y Growth</span></div>
<div class="divider" style="left:703px"></div>
<div class="stat" style="left:746px"><b>2000+</b><span>Professionals in our network</span></div>
<p class="abs stats-text">Lorem ipsum dolor sit amet, consectetur adipiscing elit, sed do eiusmod tempor incididunt ut labore et dolore magna aliqua.</p>
<div class="btn btn-dark" style="left:542px;top:1970px;width:116px;height:31px">Contact Us</div>

<!-- Features -->
<section class="sec navy" style="top:2356px;height:595px">
  <div class="feat" style="left:126px;top:110px">
    <svg width="48" height="48" viewBox="0 0 48 48" fill="none" stroke="#fff" stroke-width="2"><rect x="12" y="6" width="24" height="38"/><path d="M6 44h36M17 12h4M27 12h4M17 19h4M27 19h4M17 26h4M27 26h4M21 44v-8h6v8"/></svg>
    <h4>Lorem ipsum dolor sit amet</h4><p>Lorem ipsum dolor sit amet, consectetur adipiscing elit, sed do eiusmod tempor incididunt ut labore et dolore magna</p></div>
  <div class="feat" style="left:470px;top:110px">
    <svg width="48" height="48" viewBox="0 0 48 48" fill="none" stroke="#fff" stroke-width="2"><circle cx="24" cy="24" r="19"/><ellipse cx="24" cy="24" rx="8" ry="19"/><path d="M5 24h38M9 14h30M9 34h30"/></svg>
    <h4>Lorem ipsum dolor sit amet</h4><p>Lorem ipsum dolor sit amet, consectetur adipiscing elit, sed do eiusmod tempor incididunt ut labore et dolore magna</p></div>
  <div class="feat" style="left:823px;top:110px">
    <svg width="48" height="48" viewBox="0 0 48 48" fill="none" stroke="#fff" stroke-width="2"><rect x="3" y="8" width="32" height="24"/><path d="M14 40h10M19 32v8"/><rect x="38" y="8" width="8" height="32"/></svg>
    <h4>Lorem ipsum dolor sit amet</h4><p>Lorem ipsum dolor sit amet, consectetur adipiscing elit, sed do eiusmod tempor incididunt ut labore et dolore magna</p></div>
  <div class="feat" style="left:126px;top:343px">
    <svg width="48" height="48" viewBox="0 0 48 48" fill="none" stroke="#fff" stroke-width="2"><path d="M4 16L24 5l20 11zM6 44h36M8 40h32M11 20v18M19 20v18M29 20v18M37 20v18"/></svg>
    <h4>Lorem ipsum dolor sit amet</h4><p>Lorem ipsum dolor sit amet, consectetur adipiscing elit, sed do eiusmod tempor incididunt ut labore et dolore magna</p></div>
  <div class="feat" style="left:470px;top:343px">
    <svg width="48" height="48" viewBox="0 0 48 48" fill="none" stroke="#fff" stroke-width="2"><circle cx="24" cy="24" r="19"/><path d="M24 5v38M5 24h38M12 11c6 6 18 6 24 0M12 37c6-6 18-6 24 0"/></svg>
    <h4>Lorem ipsum dolor sit amet</h4><p>Lorem ipsum dolor sit amet, consectetur adipiscing elit, sed do eiusmod tempor incididunt ut labore et dolore magna</p></div>
  <div class="feat" style="left:823px;top:343px">
    <svg width="48" height="48" viewBox="0 0 48 48" fill="none" stroke="#fff" stroke-width="2.5"><circle cx="24" cy="24" r="20"/><path d="M30 16c-2-2-4-3-6-3-4 0-6 2-6 5 0 6 12 4 12 10 0 3-3 5-6 5-3 0-5-1-7-3M24 9v30"/></svg>
    <h4>Lorem ipsum dolor sit amet</h4><p>Lorem ipsum dolor sit amet, consectetur adipiscing elit, sed do eiusmod tempor incididunt ut labore et dolore magna</p></div>
</section>

<!-- Testimonial -->
<div class="abs quote" style="left:176px;top:2990px">“</div>
<div class="abs quote" style="left:985px;top:3165px">”</div>
<h2 class="abs testi-title">What our clients say</h2>
<p class="abs testi-text">Lorem ipsum dolor sit amet, consectetur adipiscing elit, sed do eiusmod tempor incididunt ut labore et dolore magna aliqua. Ut enim ad minim veniam, quis nostrud exercitation ullamco laboris nisi ut aliquip ex ea commodo consequat. Duis aute irure dolor in reprehenderit in voluptate velit esse cillum dolore eu fugiat nulla pariatur. Excepteur sint occaecat cupidatat non proident, sunt in culpa qui officia deserunt mollit anim id est laborum.</p>
<div class="abs testi-name">John Smith</div>
<div class="abs testi-role">His Company Name</div>

<!-- Contact -->
<section class="sec navy" style="top:3267px;height:634px">
  <div class="ring ring-w" style="left:705px;top:-10px;width:920px;height:920px"></div>
  <div class="photo" role="img" aria-label="Hand tapping a glowing phone surrounded by digital payment icons" style="left:752px;top:18px;width:860px;height:860px;background:radial-gradient(circle at 30% 45%,#3fd0ff,#2a6ee0 35%,#7a3fb8 65%,#1a1c60)"></div>
  <h2 class="abs" style="left:141px;width:487px;top:80px;text-align:center;font-size:26px;font-weight:600">Contact Us</h2>
  <p class="abs" style="left:141px;width:487px;top:123px;text-align:center;font-size:11px;line-height:17px">Lorem ipsum dolor sit amet, consectetur adipiscing elit<br>sed do eiusmod tempor</p>
  <div class="field" style="top:171px;height:36px">Name</div>
  <div class="field" style="top:224px;height:36px">Email</div>
  <div class="field" style="top:277px;height:36px">Contact Number</div>
  <div class="field" style="top:330px;height:106px">Your Message</div>
  <div class="btn btn-solid" style="left:141px;top:457px;width:120px;height:36px;font-size:13px;font-weight:500">Submit</div>
  <p class="abs" style="left:141px;width:487px;top:519px;text-align:center;font-size:15px;font-weight:500">Call us Today : 0100-55501-2200</p>
  <p class="abs" style="left:141px;width:487px;top:543px;text-align:center;font-size:11px">info@veridanpay.com</p>
</section>

<!-- Map -->
<div class="sec" role="img" aria-label="Street map showing the office location" style="top:3901px;height:418px;background:linear-gradient(180deg,#eef0f2,#e4e8ea)"></div>
<svg class="abs" style="left:614px;top:4018px" width="26" height="34" viewBox="0 0 26 34"><path d="M13 1C6 1 1 6 1 13c0 9 12 20 12 20s12-11 12-20C25 6 20 1 13 1z" fill="#0d1b5e"/><circle cx="13" cy="13" r="5" fill="#fff"/></svg>

<!-- Footer -->
<section class="sec navy" style="top:4319px;height:199px">
  <div class="brand" style="left:141px;top:38px"><span class="brand-dot"></span><span class="brand-name">Veridan</span></div>
  <p class="abs" style="left:141px;top:109px;width:160px;font-size:8px;line-height:11px">Lorem ipsum dolor sit amet, consectetur adipiscing elit, sed do eiusmod tempor incididunt ut labore et dolore magna aliqua. Ut enim ad minim veniam, quis nostrud exercitation.</p>
</section>
<div class="foot-col" style="left:427px"><h5>Pages</h5>Services<br>About Us<br>Blog<br>Contact Us</div>
<div class="foot-col" style="left:618px"><h5>Contact</h5>
  <div>☏ 1300 555 014</div><div>☏ 1300 555 014</div><div>✉ support@veridanpay.com</div><div style="line-height:13px;width:130px">⌖ 12 Harbour Lane, Eastbrook 4100</div></div>
<div class="social" style="left:618px"></div>
<div class="social" style="left:648px"></div>
<div class="social" style="left:678px"></div>
<div class="foot-col" style="left:868px"><h5>Subscribe to our News Letters</h5></div>
<div class="sub-field" style="top:4374px">Name</div>
<div class="sub-field" style="top:4421px">Email</div>
<div class="btn btn-solid" style="left:957px;top:4472px;width:98px;height:28px">Subscribe</div>
<div class="sec" style="top:4518px;height:31px;background:var(--bar);color:#fff;font-size:9px;text-align:center;line-height:31px">Copyright © 2021 veridanconsulting. All Rights Reserved</div>

</body>
</html>
```